How likely are people to engage in social distancing? We need a good illustration to show the data!

We surveyed U.S. adults March 20th - 24th, 2020 and asked how likely they were to engage in social distancing (and other COVID-19 related health behaviors). What did the survey find? Basically, most people intend to engage in social distancing behaviors (e.g., avoiding large crowds) and other behaviors that reduce the spread of COVID-19 (e.g., washing hands at least 20 seconds). When most people intend to engage in a behavior, then public health professionals try to leverage that to move more people to act.
Now we need innovative and professional images that attempt to communicate one or all of these findings. The specific findings are nicely summarized in the attached document. For example, 82% of participants intend to engage in social distancing.
What sort of visual are we looking for? Our preference is for an original illustration (or set of illustrations). Our preference is for (creative and powerful illustrations, but we are also open to the creative and well-executed infographics.
We need these images fast . We will award monetary prizes to the 3 best designs. If we like more than that, then we might purchase more (e.g., in past contests, we have purchased as many as 30 designs).
What we will need:
(1) The illustrations must be original and we will need the photoshop and/or illustrator files for all artwork.
(2) You can illustrate all of the findings or just one of them. We need creative approaches that do a lucid job of bringing the data to life. Most people intend to engage in these behaviors. How to communicate that? Corvantists and Halmerites do not differ in their intentions; how to communicate that?
(3) The illustration should say, somewhere: "Based on a survey of 400 U.S. adults conducted March 20 - 24th, 2020."

U.S. Adults

• Original illustrations based on the findings of the survey (see attached document).

```html
<!DOCTYPE html>
<html lang="en">
<head>
<meta charset="utf-8">
<title>Survey of 400 U.S. adults – intended health behaviours</title>
<link href="https://fonts.googleapis.com/css2?family=Tinos:wght@400;700&display=swap" rel="stylesheet">
<style>
  :root {
    --navy: #1e3457;
    --canvas: #c4c5c7;
    --card: #ffffff;
    --ink: #111111;
    --blue: #2f6fc4;
    --red: #d1332e;
    --grid: #d9d9d9;
  }
  * { margin: 0; padding: 0; box-sizing: border-box; }
  html, body { width: 675px; height: 1200px; overflow: hidden; }
  body {
    position: relative;
    background: var(--canvas);
    font-family: "Tinos", "Times New Roman", serif;
    color: var(--ink);
  }
  .header {
    position: absolute; left: 0; top: 0; width: 675px; height: 96px;
    background: var(--navy); color: #fff; text-align: center;
  }
  .header .lead { font-size: 17px; padding-top: 6px; }
  .header .title { font-size: 40px; font-weight: 700; line-height: 42px; }
  .header .dates { font-size: 19px; font-weight: 700; }
  .subtitle {
    position: absolute; top: 104px; left: 0; width: 675px;
    text-align: center; font-size: 16px;
  }
  .behaviour { position: absolute; width: 148px; text-align: center; }
  .behaviour .label {
    height: 34px; display: flex; align-items: flex-end; justify-content: center;
    font-size: 14px; line-height: 15px;
  }
  .behaviour .picture {
    margin-top: 6px; height: 124px; background: var(--card); padding: 6px;
  }
  .behaviour .picture div { width: 100%; height: 100%; }
  .behaviour .pct { margin-top: 18px; font-size: 30px; font-weight: 700; }
  .handshake {
    position: absolute; left: 228px; top: 630px; width: 220px; height: 120px;
    background: radial-gradient(ellipse at center, #3a3a3a 0%, #6b6b6b 55%, rgba(196,197,199,0) 72%);
  }
  .party {
    position: absolute; top: 676px; display: flex; align-items: center; gap: 7px;
    font-size: 18px; font-weight: 700;
  }
  .party .dot { width: 14px; height: 14px; border-radius: 50%; }
  .party.corvantist { left: 18px; color: var(--red); }
  .party.corvantist .dot { background: var(--red); }
  .party.halmerite { right: 18px; color: var(--blue); }
  .party.halmerite .dot { background: var(--blue); }
  .chart {
    position: absolute; left: 90px; top: 910px; width: 506px; height: 262px;
    background: #fff;
  }
  .chart svg { display: block; font-family: "Tinos", "Times New Roman", serif; }
</style>
</head>
<body>
  <header class="header">
    <div class="lead">Based on a</div>
    <div class="title">survey of 400 U.S. adults</div>
    <div class="dates">conducted March 20 - 24th, 2020</div>
  </header>

  <p class="subtitle">Percentage of Americans intending to engage in:</p>

  <section class="behaviour" style="left:11px;top:108px">
    <div class="label">social distancing</div>
    <div class="picture"><div role="img" aria-label="Two people standing apart with an arrow between them" style="background:linear-gradient(180deg,#f2f2f2,#d6d6d6)"></div></div>
    <div class="pct">82%</div>
  </section>
  <section class="behaviour" style="left:180px;top:108px">
    <div class="label">Work from home</div>
    <div class="picture"><div role="img" aria-label="Person working at a desk with a cat" style="background:linear-gradient(180deg,#ececec,#b9bcc4)"></div></div>
    <div class="pct">63%</div>
  </section>
  <section class="behaviour" style="left:349px;top:108px">
    <div class="label">Avoid large gatherings</div>
    <div class="picture"><div role="img" aria-label="Crowd of people crossed out with a prohibition sign" style="background:linear-gradient(180deg,#b89a86,#7d6a60)"></div></div>
    <div class="pct">85%</div>
  </section>
  <section class="behaviour" style="left:518px;top:108px">
    <div class="label">Cancel social activities</div>
    <div class="picture"><div role="img" aria-label="Friends at a table crossed out with a prohibition sign" style="background:linear-gradient(180deg,#e6ddd3,#bda992)"></div></div>
    <div class="pct">81%</div>
  </section>

  <section class="behaviour" style="left:11px;top:330px">
    <div class="label">Put distance between yourself and other people</div>
    <div class="picture"><div role="img" aria-label="Three people standing spaced apart" style="background:linear-gradient(180deg,#f0f0f0,#c9ccd2)"></div></div>
    <div class="pct">85%</div>
  </section>
  <section class="behaviour" style="left:180px;top:330px">
    <div class="label">Wash hands at least 20 seconds</div>
    <div class="picture"><div role="img" aria-label="Hands being washed under a tap" style="background:linear-gradient(180deg,#e4e6ea,#a9adb4)"></div></div>
    <div class="pct">87%</div>
  </section>
  <section class="behaviour" style="left:349px;top:330px">
    <div class="label">Use hand sanitizer</div>
    <div class="picture"><div role="img" aria-label="Hands rubbing in sanitizer" style="background:linear-gradient(180deg,#f4f4f4,#d2d2d2)"></div></div>
    <div class="pct">85%</div>
  </section>
  <section class="behaviour" style="left:518px;top:330px">
    <div class="label">Avoid touching your eyes, nose, and mouth</div>
    <div class="picture"><div role="img" aria-label="Person touching their face crossed out with a prohibition sign" style="background:linear-gradient(180deg,#ead8c8,#b99a80)"></div></div>
    <div class="pct">81%</div>
  </section>

  <div class="party corvantist"><span class="dot"></span>Corvantists</div>
  <div class="handshake" role="img" aria-label="Two hands in a handshake"></div>
  <div class="party halmerite">Halmerites<span class="dot"></span></div>

  <figure class="chart">
    <svg width="506" height="262" viewBox="0 0 506 262" role="img" aria-label="Bar chart comparing Corvantists and Halmerites on each behaviour">
      <text x="253" y="22" text-anchor="middle" font-size="14" fill="#333">Comparing Corvantists and Halmerites</text>
      <g stroke="var(--grid)" stroke-width="1">
        <line x1="180" y1="34" x2="180" y2="206"/><line x1="240" y1="34" x2="240" y2="206"/>
        <line x1="300" y1="34" x2="300" y2="206"/><line x1="360" y1="34" x2="360" y2="206"/>
        <line x1="420" y1="34" x2="420" y2="206"/><line x1="480" y1="34" x2="480" y2="206"/>
      </g>
      <g font-size="9" fill="#333" text-anchor="end">
        <text x="174" y="46">Avoid touching your eyes, nose, and mouth</text>
        <text x="174" y="67">Use hand sanitizer</text>
        <text x="174" y="88">Wash hands at least 20 seconds</text>
        <text x="174" y="109">Put distance between yourself and other...</text>
        <text x="174" y="130">Cancel social activities</text>
        <text x="174" y="151">Avoid large gatherings</text>
        <text x="174" y="172">Work from home</text>
        <text x="174" y="193">social distancing</text>
      </g>
      <g fill="var(--red)">
        <rect x="180" y="37" width="240" height="7"/>
        <rect x="180" y="58" width="252" height="7"/>
        <rect x="180" y="79" width="258" height="7"/>
        <rect x="180" y="100" width="252" height="7"/>
        <rect x="180" y="121" width="240" height="7"/>
        <rect x="180" y="142" width="252" height="7"/>
        <rect x="180" y="163" width="180" height="7"/>
        <rect x="180" y="184" width="240" height="7"/>
      </g>
      <g fill="var(--blue)">
        <rect x="180" y="44" width="246" height="7"/>
        <rect x="180" y="65" width="258" height="7"/>
        <rect x="180" y="86" width="264" height="7"/>
        <rect x="180" y="107" width="258" height="7"/>
        <rect x="180" y="128" width="246" height="7"/>
        <rect x="180" y="149" width="258" height="7"/>
        <rect x="180" y="170" width="198" height="7"/>
        <rect x="180" y="191" width="252" height="7"/>
      </g>
      <g font-size="10" fill="#333" text-anchor="middle">
        <text x="180" y="220">0</text><text x="240" y="220">20</text><text x="300" y="220">40</text>
        <text x="360" y="220">60</text><text x="420" y="220">80</text><text x="480" y="220">100</text>
      </g>
      <g font-size="11" fill="#333">
        <rect x="170" y="238" width="9" height="9" fill="var(--blue)"/>
        <text x="184" y="246">Halmerite</text>
        <rect x="262" y="238" width="9" height="9" fill="var(--red)"/>
        <text x="276" y="246">Corvantist</text>
      </g>
    </svg>
  </figure>
</body>
</html>
```